Business card/stationary for non profit organization
Business card and Stationary for non profit organization
Business card/stationary for non profit organization - Children
Creative Brief
Bright & Fun-filled
Mr. Fenwick
Founder
517 Bellmore Lane Suite 309 Harwell, New York 10592
fenwick@mrfenwickcommons.org
www.mrfenwickcommons.org
Please have the logo on the back of the business card and room for a tagline.
Concepts
Business Cards for kids golf

```html
<!DOCTYPE html>
<html lang="en">
<head>
<meta charset="utf-8">
<title>Mr. Fenwick's Commons – Business Card</title>
<link href="https://fonts.googleapis.com/css2?family=Roboto:wght@400;700;900&display=swap" rel="stylesheet">
<style>
  :root {
    --backdrop: #8f8f8f;
    --gold-light: #e3d57a;
    --gold-mid: #bfa83a;
    --gold-dark: #8a7418;
    --ink: #111111;
    --paper: #ffffff;
    --text-dark: #1c1c1c;
  }
  * { margin: 0; padding: 0; box-sizing: border-box; }
  html, body { width: 1200px; height: 908px; overflow: hidden; }
  body {
    background: var(--backdrop);
    font-family: "Roboto", Arial, sans-serif;
    position: relative;
  }
  .card {
    position: absolute;
    left: 250px;
    width: 700px;
    height: 400px;
    border-radius: 22px;
    overflow: hidden;
  }
  .card-back {
    top: 40px;
    background: radial-gradient(ellipse at 40% 35%, var(--gold-light), var(--gold-mid) 55%, var(--gold-dark));
    display: flex;
    align-items: center;
    justify-content: center;
  }
  .card-front { top: 468px; background: var(--paper); }
  .brand {
    display: flex;
    align-items: center;
    gap: 14px;
    color: var(--ink);
    font-weight: 900;
    text-transform: uppercase;
  }
  .brand-dot { border-radius: 50%; background: var(--ink); flex: none; }
  .card-back .brand { font-size: 34px; }
  .card-back .brand-dot { width: 44px; height: 44px; }
  .front-shapes { position: absolute; inset: 0; }
  .identity {
    position: absolute;
    right: 36px;
    top: 124px;
    text-align: right;
    color: var(--paper);
  }
  .identity-name { font-size: 30px; font-weight: 700; }
  .identity-role { font-size: 18px; }
  .front-brand {
    position: absolute;
    left: 34px;
    top: 176px;
    width: 230px;
  }
  .front-brand .brand { font-size: 20px; line-height: 1.15; gap: 12px; }
  .front-brand .brand-dot { width: 64px; height: 64px; }
  .contact {
    position: absolute;
    left: 300px;
    top: 232px;
    color: var(--text-dark);
    font-size: 15px;
    line-height: 1.35;
  }
  .contact-address { margin-bottom: 6px; }
  .contact-line { display: flex; align-items: center; gap: 8px; }
  .contact-icon { width: 12px; height: 12px; border-radius: 50%; background: var(--text-dark); flex: none; }
</style>
</head>
<body>
  <section class="card card-back">
    <div class="brand"><span class="brand-dot"></span>Mr. Fenwick's Commons</div>
  </section>

  <section class="card card-front">
    <svg class="front-shapes" width="700" height="400" viewBox="0 0 700 400" aria-hidden="true">
      <defs>
        <linearGradient id="goldBand" x1="0" y1="0" x2="1" y2="1">
          <stop offset="0" stop-color="#e3d57a"/>
          <stop offset="0.5" stop-color="#bfa83a"/>
          <stop offset="1" stop-color="#8a7418"/>
        </linearGradient>
      </defs>
      <polygon points="0,215 330,215 380,195 700,195 700,400 0,400" fill="url(#goldBand)"/>
      <polygon points="380,110 700,110 700,195 380,195 340,152" fill="#111111"/>
    </svg>
    <div class="identity">
      <div class="identity-name">Mr. Fenwick</div>
      <div class="identity-role">Founder</div>
    </div>
    <div class="front-brand">
      <div class="brand"><span class="brand-dot"></span><span>Mr. Fenwick's<br>Commons</span></div>
    </div>
    <div class="contact">
      <div class="contact-address">517 Bellmore Lane Suite 309<br>Harwell, New York 10592</div>
      <div class="contact-line"><span class="contact-icon"></span>914-555-0182</div>
      <div class="contact-line"><span class="contact-icon"></span>914-555-0147</div>
      <div class="contact-line"><span class="contact-icon"></span>fenwick@mrfenwickcommons.org</div>
      <div class="contact-line"><span class="contact-icon"></span>www.mrfenwickcommons.org</div>
    </div>
  </section>
</body>
</html>
```